Vallée douce coffee - Label design

Watchout: Keep in mind while you submit it needs to be a LABEL (that will be sticked on brown kraft 250 g side gusset coffee pouches). No custom pack for time being (need more scale to custom print pack).

Looking for a label design for my new Beau Matin collection of freshly roasted, single origin specialty coffee. Brand name is Vallée Douce (it means red earth and alludes to the soil coffee grows on at high altitude in Africa. It also alludes to the red color of the coffee fruit). Brand selling line is "Pure Origin Coffee". Label to go as stickers on 250 g side gusset coffee pouches in Kraft brown paper (will print labels and stick on packs, packs are 80 mm wide and 260 mm long). This is a relatively complex project comprising the "vallée douce" brand logo (funded separately, winner will have the job), the "Beau Matin" collection visual identity, iconic assets for brand and collection recognition across lineup, educational visual icons, text placeholders. It needs to combine hard point visual elements and soft points (text placeholder) which I can easily edit on need basis (text needs to be "outlines" for easy editing after submission). Winner of label submission gets to design brand logo. I will ultimately need 3 different labels for our Beau Matin collection, one for each continent our coffee comes from (Africa, Asia, Latin America). This pitch should focus on the Africa one only. Winner will then have opportunity to design the other ones in consistent way.

BRIEF:
We roast single origin, high quality specialty coffee from high altitude estates in Africa (volcanic slopes in Congo and Burundi, Highlands in Ethiopia and Kenya) Design need to induce the premiumness of the proposition (this is a collection called "Beau Matin"), as well the the unique geographical origins of our coffee (without being too specific as we want to use same label for all our African origins) -oversized shape of continent in background + some visuals conveying the African roots could work well. It needs to create a mental Journey "back to the origins" - of mankind, of unique terroirs creating the best coffee, of our unspoilt roots. So the Journey themes is critical (to be expressed by the telegram type of font, by the way Africa is brought to life,etc.). At the same time keep in mind label space is limited (label stickers go on 250 g coffee pouches made in kraft brown paper) and we want to have a pure design, which leaves room to the text placeholder (see below) and is easily recognizable and reapplicable across the SKUs (we will add Asia and Latin America packs once we lock Africa). As such we need to strike right balance between visual differentiation by origin (Africa, Asia, Latin America) and common iconic assets for brand recognition and lineup harmonization (same font, same way the continent is brought to life, same structure of the label, differentiation by color background,etc.).

We need placeholder for text that will specify exact name of estate, county of origin, coffee type, roasting level and tasting notes. Here I will allow myself some creative direction: it should be in the format of a vintage luggage tag (see attached examples) where we can edit content in Telegram font (our coffee sourcing changes often). We will need to assess if the tag remains standard across collection, or whether we are able to give it a visual twist for each origin (Africa, Asia, Latin America). That would be nicer (see Moonpeak "Ledgers" example), but priority of the text placeholder is clarity of information above anything else.

Last nice to have (if it time allows) we need educational visual icons (ideally as separate small round labels we can stick on the pack above the main label) for recommended brewing method (filter, espresso, italian moka, french press).

Reason: Still looking for the design in line with brief. Will send feedback to the top 3 routes today.

Target Market(s)

Switzerland

Industry/Entity Type

Coffee Shop

Logo Text

Vallée douce -Pure Origin Coffee

Font styles to use
Other font styles liked:
• TELEGRAM type of font to induce geographical journey, single origin,.. For the "luggage tag" placeholder

Requirements
Must have
• - Brand name: Vallée Douce. Brand selling line: Pure Origin Coffee. Brand Logo: winner of label submission gets to design brand logo
• - Collection name: BEAU MATIN (written, I can see well as a vertical block). name of SKU: AFRICA (visualized a must, written tbc).
• - Text place holder (vintage luggage tag in telegram font) : we will show there name of estate, country of origin, tasting notes. I could see nicely a baggage tag format, where we fill in the details in telegram type of font.
• - 100% single origin Arabica (at the bottom)
• - 250 g (at the bottom)
• Technical Specs:
• A. Artwork must be supplied in either Adobe illustrator or Adobe Photoshop files or Coral Draw files
• B. Create all text in artwork in ‘ outlines ’
• C. The resolution of photographic image files must be no less than 350 dpi
• D. Never flatten the file as we require all layers
• E. All Photoshop image files should be linked and attached. Never flatten the layers and do not change the directory
• F. Create the images with CMYK colour mode ( RGB colour mode is not for printing)
• G. If you are going to use a spot colour please reference the Pantone ( PMS #)
• H. Designate all ‘Transparent’ areas in the artwork with a custom Pantone colour as well as designating the layer’s name as ‘ Transparent’. Please indicate specifically which pantone colour is designated for the ‘transparent’ area.
• I. Reduce any barcodes to 85% as a minimum scale
Nice to have
• - educational simple visual icons on recommended brewing method (filer, italian moka, french press or espresso) as additional small stickers to stick above main label

```html
<!DOCTYPE html>
<html lang="en">
<head>
<meta charset="utf-8">
<title>Vallée Douce – Beau Matin Africa Label</title>
<link rel="stylesheet" href="https://fonts.googleapis.com/css2?family=Kaushan+Script&family=Noto+Serif:wght@400&family=Open+Sans:wght@400;500;600;700&display=swap">
<style>
  :root {
    --roast-brown: #5e2b27;
    --bean-light: #8a5a50;
    --label-cream: #fdfcef;
    --die-cut-grey: #a8a8a8;
    --canvas-white: #ffffff;
    --frame-grey: #7a7a7a;
  }
  html, body {
    margin: 0;
    padding: 0;
    width: 1200px;
    height: 1125px;
    overflow: hidden;
    background: var(--canvas-white);
  }
  .artboard {
    width: 1200px;
    height: 1125px;
    box-sizing: border-box;
    border: 1px solid var(--frame-grey);
  }
  .artboard svg { display: block; }
  .label-base { fill: var(--label-cream); stroke: var(--die-cut-grey); stroke-width: 1; }
  .label-frame-thick { fill: none; stroke: var(--roast-brown); stroke-width: 4; }
  .label-frame-thin { fill: none; stroke: var(--roast-brown); stroke-width: 1.6; }
  .hang-hole { fill: var(--label-cream); stroke: var(--roast-brown); stroke-width: 5; }
  .selling-line {
    font-family: "Noto Serif", Georgia, serif;
    font-size: 22px;
    fill: var(--roast-brown);
  }
  .name-band { fill: var(--roast-brown); }
  .stitch { stroke: var(--label-cream); stroke-width: 2.6; stroke-linecap: round; stroke-dasharray: 0 7.6; }
  .brand-name {
    font-family: "Kaushan Script", cursive;
    font-size: 44px;
    fill: var(--label-cream);
  }
  .rule { stroke: var(--roast-brown); stroke-width: 1.6; }
  .purity {
    font-family: "Open Sans", Arial, sans-serif;
    font-size: 33px;
    fill: var(--roast-brown);
  }
  .origin-line {
    font-family: "Open Sans", Arial, sans-serif;
    font-size: 15px;
    fill: var(--roast-brown);
  }
  .variety {
    font-family: "Open Sans", Arial, sans-serif;
    font-size: 17px;
    font-weight: 700;
    fill: var(--roast-brown);
  }
  .collection-name {
    font-family: "Open Sans", Arial, sans-serif;
    font-size: 29px;
    font-weight: 600;
    fill: var(--roast-brown);
  }
  .bean-art { fill: url(#beanTone); }
  .continent {
    font-family: "Open Sans", Arial, sans-serif;
    font-size: 19px;
    font-weight: 700;
    fill: var(--roast-brown);
  }
</style>
</head>
<body>
<main class="artboard">
  <svg width="1198" height="1123" viewBox="0 0 960 900" xmlns="http://www.w3.org/2000/svg">
    <defs>
      <path id="labelShape" d="M312 245 Q326 240 328 222 L392 214 C420 212 430 183 480 183 C530 183 540 212 568 214 L632 222 Q634 240 648 245 L648 640 Q634 645 632 660 C575 665 545 697 480 697 C415 697 385 665 328 660 Q326 645 312 640 Z"/>
      <radialGradient id="beanTone" cx="50%" cy="50%" r="60%">
        <stop offset="0%" stop-color="var(--bean-light)"/>
        <stop offset="100%" stop-color="var(--roast-brown)"/>
      </radialGradient>
    </defs>

    <g class="label">
      <use href="#labelShape" class="label-base"/>
      <use href="#labelShape" class="label-frame-thick" vector-effect="non-scaling-stroke"
           transform="translate(480 440) scale(0.955 0.972) translate(-480 -440)"/>
      <use href="#labelShape" class="label-frame-thin" vector-effect="non-scaling-stroke"
           transform="translate(480 440) scale(0.925 0.952) translate(-480 -440)"/>

      <circle class="hang-hole" cx="480" cy="220" r="8"/>

      <text class="selling-line" x="480" y="277" text-anchor="middle" textLength="250" lengthAdjust="spacingAndGlyphs">PURE ORIGIN COFFEE</text>

      <rect class="name-band" x="333" y="298" width="294" height="98"/>
      <line class="stitch" x1="338" y1="307" x2="624" y2="307"/>
      <line class="stitch" x1="338" y1="387" x2="624" y2="387"/>
      <text class="brand-name" x="480" y="364" text-anchor="middle" textLength="244" lengthAdjust="spacingAndGlyphs">Vallée Douce</text>

      <line class="rule" x1="372" y1="462" x2="410" y2="462"/>
      <line class="rule" x1="541" y1="462" x2="584" y2="462"/>
      <text class="purity" x="482" y="463" text-anchor="middle">100%</text>
      <text class="origin-line" x="475" y="492" text-anchor="middle" letter-spacing="0.5">SINGLE ORIGIN</text>
      <text class="variety" x="478" y="515" text-anchor="middle">ARABICA</text>

      <line class="rule" x1="372" y1="540" x2="427" y2="540"/>
      <line class="rule" x1="525" y1="540" x2="584" y2="540"/>
      <text class="collection-name" x="481" y="573" text-anchor="middle" textLength="184" lengthAdjust="spacingAndGlyphs">BEAU MATIN</text>
      <line class="rule" x1="372" y1="579" x2="427" y2="579"/>
      <line class="rule" x1="525" y1="579" x2="584" y2="579"/>

      <rect class="bean-art" x="445" y="590" width="68" height="40" rx="20" role="img" aria-label="Illustration of two roasted coffee beans"/>

      <text class="continent" x="483" y="663" text-anchor="middle">Africa</text>
    </g>
  </svg>
</main>
</body>
</html>
```